Real Estate Agent needs business card design

We have logo designed already, want to have business card designed. Very interested in those smaller size business card as they look very trendy. Business name is called TOVANE REALTY

Industry/Entity Type

Business

```html
<!DOCTYPE html>
<html lang="en">
<head>
<meta charset="utf-8">
<title>Tovane Realty – Business Card</title>
<link rel="stylesheet" href="https://fonts.googleapis.com/css2?family=Crimson+Text:ital@0;1&family=Sorts+Mill+Goudy&display=swap">
<style>
  :root {
    --backdrop: #e6e6e6;
    --gold-light: #b7965f;
    --gold-dark: #a68350;
    --charcoal: #2f2f31;
    --paper: #f6f6f5;
    --ink: #222222;
    --accent: #a9844f;
    --white: #ffffff;
  }
  * { margin: 0; padding: 0; box-sizing: border-box; }
  html, body {
    width: 1200px;
    height: 576px;
    overflow: hidden;
    background: var(--backdrop);
  }
  .canvas {
    position: relative;
    width: 1200px;
    height: 576px;
  }
  .card {
    position: absolute;
    border-radius: 14px;
    overflow: hidden;
  }
  .card-front {
    left: 82px;
    top: 138px;
    width: 484px;
    height: 294px;
    background: linear-gradient(180deg, var(--gold-light), var(--gold-dark));
  }
  .brand-disc {
    position: absolute;
    left: 144px;
    top: 50px;
    width: 194px;
    height: 194px;
    border-radius: 50%;
    background: var(--charcoal);
    display: flex;
    align-items: center;
    justify-content: center;
  }
  .brand-name {
    font-family: "Crimson Text", serif;
    font-variant: small-caps;
    font-size: 22px;
    letter-spacing: 0.5px;
    color: var(--white);
    white-space: nowrap;
  }
  .card-back {
    left: 602px;
    top: 138px;
    width: 480px;
    height: 290px;
    background: var(--paper);
    text-align: center;
    font-family: "Crimson Text", serif;
    color: var(--ink);
  }
  .contact {
    position: absolute;
    left: 0;
    right: 0;
    top: 82px;
  }
  .person-name {
    font-family: "Sorts Mill Goudy", serif;
    font-size: 21px;
    line-height: 26px;
    color: var(--accent);
    font-weight: 400;
  }
  .person-role {
    font-style: italic;
    font-size: 11.5px;
    line-height: 14px;
  }
  .address {
    margin-top: 16px;
    font-size: 12.5px;
    line-height: 16px;
    font-style: normal;
  }
  .phone, .web {
    font-size: 12.5px;
    line-height: 16px;
  }
  .phone { margin-top: 5px; }
  .web-domain { color: var(--accent); }
</style>
</head>
<body>
  <main class="canvas">
    <section class="card card-front" aria-label="Card front">
      <div class="brand-disc">
        <span class="brand-name">Tovane Realty</span>
      </div>
    </section>

    <section class="card card-back" aria-label="Card back">
      <div class="contact">
        <h1 class="person-name">Hannah Lowell</h1>
        <p class="person-role">Senior Property Consultant</p>
        <address class="address">7C, 148 Harbour Road,<br>Westbrook, NSW 2081</address>
        <p class="phone">0491 570 156</p>
        <p class="web">www.<span class="web-domain">tovanerealty</span>.com.au</p>
      </div>
    </section>
  </main>
</body>
</html>
```